Web site homepage

I need a new homepage designing for a consumer based IT project

The obvious web sites I like are comparison sites, as they clearly work. See http://www.pricelarder.example/shopping/ca/anti-virus-security-data-protection-c610167/

However this isn’t as clean as it could be as its not their primary revenue stream. However the “results” page for one of the internal pages, should have a theme like this. You will see that by clicking on the product’s image, it takes you straight to the vendor’s check out page – which is exactly the same for the results by on my web site.

Although a completely different market, I like the https://www.quellbrook.example/ web site for its simplicity in selecting your product (pay day loan amount), through to transaction completion. Has a very consumer and friendly feel to it.

I have attached some previous designs which were ok, but not great. I don't want the 4 boxes in the middle anymore but I do like the feel with the top page images

I have also attached a jpeg of the logo I wish to use
Updates

Project Deadline Extended
Reason: A lot of the designs seem to have missed that I DO NOT require the 4 selection boxes as provided in the previous designs I issued as a guide. I am subsequently getting a lot of designs that contain this. I also seem to have a lot of designs which include product images. I DO NOT want these (at this time). The initial purpose of the site is informational. I am extending the deadline so that I can give feedback to each design and for you to provide a response. I will not extend past these extra 5 days. Thanks

Hello designers, Thank you all for the efforts you have gone to, it is appreciated. I have reviewed each an every design giving my honest feedback. If you have not received the feedback, please contact me. I have extended the deadline - and WILL NOT be extending this any further. I will be reviewing each updated design at this time every evening until the contest closes to give you the feedback as quickly as possible. Thanks for your efforts and please contact me to discuss any points. Gareth.

Target Market(s)

Shieldwise Hub will be an affiliate based web site providing a product comparison-based service for the consumer market, specifically for the UK. Target audience is 100% consumer and should be easy, friendly and memorable for the user.

Industry/Entity Type

Loan

Font styles to use
Sans Serif

Colors

Designer to choose colors to be used in the design.

Requirements
Must have
• Much be a bold, friendly and simple layout
Should not have
• corporate feel. must be consumer focused. bold and simple

```html
<!DOCTYPE html>
<html lang="en">
<head>
<meta charset="utf-8">
<title>Shieldwise Hub – Compare Computer Security Software</title>
<link href="https://fonts.googleapis.com/css2?family=Open+Sans:wght@400;600;700;800&display=swap" rel="stylesheet">
<style>
:root{
  --navy:#16345f;
  --blue:#1f4f8e;
  --blue-light:#3f7fc6;
  --hero-a:#0f2746;
  --hero-b:#24528a;
  --orange:#f7941d;
  --orange-dark:#e07b0a;
  --grey-bg:#e6e9ee;
  --grey-line:#d6dbe2;
  --text:#3c4350;
  --muted:#8a919c;
  --white:#ffffff;
  --footer:#0f2645;
}
*{box-sizing:border-box;margin:0;padding:0}
html,body{width:1200px;height:2204px;overflow:hidden}
body{font-family:"Open Sans",Arial,sans-serif;color:var(--text);background:var(--grey-bg);position:relative}
.wrap{width:760px;margin:0 auto;position:relative}

/* header */
.site-header{height:58px;background:var(--white)}
.site-header .wrap{height:58px;display:flex;align-items:center;justify-content:space-between}
.brand{display:flex;align-items:center;gap:8px;font-weight:700;font-size:17px;color:var(--blue)}
.brand-mark{width:22px;height:22px;background:var(--blue);border-radius:3px}
.phone{background:var(--orange);color:var(--white);font-size:11px;font-weight:700;padding:5px 10px;border-radius:3px;display:flex;align-items:center;gap:6px}
.main-nav{height:30px;background:var(--blue)}
.main-nav ul{list-style:none;display:flex;height:30px;align-items:center;padding-left:12px}
.main-nav li{color:var(--white);font-size:11px;font-weight:700;padding:0 14px;letter-spacing:.2px}

/* hero */
.hero{height:380px;background:radial-gradient(ellipse at 50% 40%,var(--hero-b),var(--hero-a) 75%);position:relative}
.hero .wrap{height:380px}
.hero-visual{position:absolute;left:20px;top:50px;width:260px;height:260px;border-radius:6px;background:linear-gradient(160deg,#c9d4e2,#7d93b1 60%,#3d5a82)}
.hero-box{position:absolute;left:290px;top:150px;width:80px;height:120px;border-radius:3px;background:linear-gradient(160deg,#e2e6ec,#b23a3a 55%,#7a1f1f)}
.hero-copy{position:absolute;left:380px;top:70px;width:370px;text-align:center;color:var(--white)}
.hero-copy h1{font-size:31px;font-weight:700;line-height:1.15}
.hero-copy h1 span{display:block;font-size:24px;font-weight:600}
.hero-cta{position:absolute;left:400px;top:290px;display:flex;align-items:center;gap:16px}
.hero-cta p{color:var(--white);font-size:17px;font-weight:700;font-style:italic}
.btn-orange{background:var(--orange);color:var(--white);font-weight:700;font-size:13px;padding:11px 20px;border-radius:3px;border-bottom:3px solid var(--orange-dark)}
.slide-arrow{position:absolute;top:180px;width:30px;height:30px;border:2px solid rgba(255,255,255,.7);border-radius:50%;display:flex;align-items:center;justify-content:center}
.slide-arrow.prev{left:-20px}.slide-arrow.next{right:-20px}

/* content */
.content{padding-top:14px;height:946px}
.panel{background:var(--white);display:flex;padding:8px;gap:8px;height:920px}
.sidebar{width:168px}
.side-block{border:1px solid var(--grey-line);margin-bottom:12px}
.side-block h3{background:var(--blue);color:var(--white);font-size:10px;font-weight:700;padding:7px 8px}
.side-block ul{list-style:none;padding:8px 8px}
.side-block li{font-size:9.5px;color:var(--text);padding:4px 0 4px 10px;position:relative;line-height:1.3}
.side-block li::before{content:"";position:absolute;left:0;top:9px;width:4px;height:4px;background:var(--orange)}
.news-item{padding:8px 8px;border-bottom:1px solid var(--grey-line)}
.news-item:last-child{border-bottom:0}
.news-item time{display:block;font-size:8px;color:var(--muted)}
.news-item p{font-size:9.5px;line-height:1.35}

.results{flex:1}
.results-head{border:1px solid var(--grey-line);padding:8px 10px;display:flex;justify-content:space-between;align-items:center}
.results-head small{font-size:8px;color:var(--muted);display:block}
.results-head h2{font-size:12.5px;color:var(--blue);font-weight:700;line-height:1.25}
.sort{font-size:9px;display:flex;align-items:center;gap:5px}
.sort span.select{border:1px solid var(--grey-line);padding:3px 22px 3px 6px;position:relative}
.offer{display:flex;align-items:center;gap:12px;border-bottom:1px solid var(--grey-line);padding:10px 6px;height:128px}
.offer-image{width:54px;height:70px;border-radius:2px;background:linear-gradient(160deg,#fff3c4,#f5b400 60%,#c98a00)}
.offer-body{flex:1}
.offer-body h4{font-size:11px;font-weight:700;color:var(--text)}
.offer-body p{font-size:9px;line-height:1.4;color:var(--muted);margin-top:3px}
.offer-body a{display:inline-block;margin-top:6px;font-size:9px;color:var(--blue-light);text-decoration:none}
.offer-body .ref{font-size:8px;color:#aab0b8;margin-top:6px}
.price{width:100px;height:76px;background:var(--orange);border-radius:3px;text-align:center;color:var(--white);padding-top:11px}
.price strong{font-size:18px;font-weight:800;display:block}
.price span{display:inline-block;margin-top:6px;background:var(--navy);font-size:9px;font-weight:700;padding:3px 10px;border-radius:2px}
.pagination{display:flex;justify-content:center;align-items:center;gap:6px;margin-top:20px;font-size:14px;font-weight:700;color:var(--text)}
.pagination .next{font-size:10px;color:var(--muted);border-left:1px solid var(--grey-line);padding-left:8px;margin-left:4px}

/* safety */
.safety{height:226px;background:var(--navy);color:var(--white)}
.safety .wrap{padding-top:22px}
.section-title{display:flex;justify-content:space-between;align-items:center;border-bottom:1px solid rgba(255,255,255,.2);padding-bottom:10px}
.section-title h2{font-size:15px;font-weight:600;letter-spacing:.5px}
.title-arrows{display:flex;gap:4px}
.title-arrows span{width:16px;height:16px;border-radius:50%;background:rgba(255,255,255,.25);display:flex;align-items:center;justify-content:center}
.articles{display:flex;gap:20px;margin-top:18px}
.article{flex:1}
.article time{font-size:8px;color:#9fb3cf}
.article h4{font-size:10.5px;font-weight:700;margin:3px 0}
.article p{font-size:9px;color:#c4d1e2;line-height:1.35}
.btn-small{display:inline-block;margin-top:8px;border:1px solid rgba(255,255,255,.4);font-size:8px;padding:3px 8px}

/* contact */
.contact{height:480px;background:var(--blue);color:var(--white)}
.contact .wrap{padding-top:50px}
.contact-title{display:flex;align-items:center;gap:16px;justify-content:center}
.contact-title::before,.contact-title::after{content:"";width:120px;height:1px;background:rgba(255,255,255,.35)}
.contact-title h2{font-size:15px;font-weight:700;letter-spacing:1px}
.contact-intro{text-align:center;font-size:10px;color:#d3def0;margin:40px auto 0;width:560px;line-height:1.5}
.contact-form{display:flex;gap:14px;margin-top:48px;padding:0 20px}
.contact-info{width:200px}
.contact-info .line,.contact-email .line{font-size:10px;display:flex;align-items:center;gap:6px;margin-bottom:12px}
.field{background:var(--white);height:24px;border-radius:2px;margin-bottom:8px;font-size:9px;color:var(--muted);padding:5px 8px}
.message{flex:1;background:var(--white);height:110px;border-radius:2px;font-size:9px;color:var(--muted);padding:6px 8px;margin-top:-4px}
.contact-email{width:150px}
.btn-send{display:flex;align-items:center;justify-content:center;background:var(--orange);font-size:18px;font-weight:700;height:60px;margin-top:2px;border-radius:2px;border-bottom:3px solid var(--orange-dark)}
.social{display:flex;justify-content:center;gap:28px;margin-top:72px;font-size:9.5px;color:#d3def0}
.social span{display:flex;align-items:center;gap:5px}
.social i{width:10px;height:10px;border-radius:50%;background:rgba(255,255,255,.5);display:inline-block}

.site-footer{height:84px;background:var(--footer);color:#8ea3c2;font-size:9px;text-align:center;padding-top:34px}
</style>
</head>
<body>

<header class="site-header">
  <div class="wrap">
    <div class="brand"><span class="brand-mark"></span>Shieldwise Hub</div>
    <div class="phone">
      <svg width="10" height="10" viewBox="0 0 24 24"><path fill="#fff" d="M6.6 10.8a15 15 0 006.6 6.6l2.2-2.2c.3-.3.7-.4 1-.2 1.1.4 2.3.6 3.6.6.6 0 1 .4 1 1V20c0 .6-.4 1-1 1A17 17 0 013 4c0-.6.4-1 1-1h3.5c.6 0 1 .4 1 1 0 1.3.2 2.5.6 3.6.1.3 0 .7-.2 1z"/></svg>
      +44 (0) 700 555 0142
    </div>
  </div>
</header>
<nav class="main-nav">
  <div class="wrap">
    <ul><li>VENDORS</li><li>PROTECTION TYPES</li><li>PRODUCTS</li><li>MARKET ANALYSIS</li><li>SHIELDWISE HUB</li></ul>
  </div>
</nav>

<section class="hero">
  <div class="wrap">
    <div class="hero-visual" role="img" aria-label="Laptop showing security shield icons with a software disc"></div>
    <div class="hero-box" role="img" aria-label="Security software product box"></div>
    <div class="hero-copy">
      <h1>Compare the Right Computer<span>Security Software</span></h1>
    </div>
    <div class="hero-cta">
      <p>... all in under 30 seconds!</p>
      <span class="btn-orange">GET STARTED</span>
    </div>
    <span class="slide-arrow prev"><svg width="10" height="12" viewBox="0 0 10 12"><path d="M7 1L2 6l5 5" stroke="#fff" stroke-width="2" fill="none"/></svg></span>
    <span class="slide-arrow next"><svg width="10" height="12" viewBox="0 0 10 12"><path d="M3 1l5 5-5 5" stroke="#fff" stroke-width="2" fill="none"/></svg></span>
  </div>
</section>

<main class="content">
  <div class="wrap panel">
    <aside class="sidebar">
      <div class="side-block">
        <h3>ANTIVIRUS PROVIDERS</h3>
        <ul><li>Wardlow</li><li>Pennock</li><li>Halvern</li><li>Tollgate</li><li>Quillmoor</li><li>Drayhurst</li><li>Embergate</li><li>Fennick</li><li>Oakrun</li><li>Marrowby</li></ul>
      </div>
      <div class="side-block">
        <h3>PROTECTION TYPES</h3>
        <ul><li>Antivirus</li><li>Firewall</li><li>Spyware</li><li>Antispam</li><li>PC Cleaning</li><li>Personal Firewall</li><li>Encryption</li><li>Safe Browsing</li><li>Zero Day Protection</li><li>Password Protection</li></ul>
      </div>
      <div class="side-block">
        <h3>LATEST NEWS</h3>
        <div class="news-item"><time>DECEMBER 12, 2013</time><p>Know which antivirus gives the best value</p></div>
        <div class="news-item"><time>DECEMBER 11, 2013</time><p>New threats target home laptops</p></div>
        <div class="news-item"><time>DECEMBER 10, 2013</time><p>Protect your family online this winter</p></div>
        <div class="news-item"><time>DECEMBER 09, 2013</time><p>Simple steps to safer passwords</p></div>
      </div>
    </aside>

    <section class="results">
      <div class="results-head">
        <div>
          <small>Anti-Virus, Security &amp; Data Protection</small>
          <h2>Compare 2362 Anti-Virus, Security<br>&amp; Data Protection offers</h2>
        </div>
        <div class="sort">Sort by: <span class="select">Relevance
          <svg style="position:absolute;right:5px;top:6px" width="7" height="5" viewBox="0 0 7 5"><path d="M0 0h7L3.5 5z" fill="#8a919c"/></svg></span></div>
      </div>

      <article class="offer">
        <div class="offer-image" role="img" aria-label="Software product box"></div>
        <div class="offer-body"><h4>Lorem ipsum dolor sit amet, consectetur elit...</h4><p>Lorem ipsum dolor sit amet, consectetur adipiscing elit, sed do eiusmod tempor incididunt ut labore et dolore.</p><a>Read more &raquo;</a><div class="ref">Shopping reference: Lorem ipsum dolor sit amet</div></div>
        <div class="price"><strong>£140.97</strong><span>Go to site</span></div>
      </article>
      <article class="offer">
        <div class="offer-image" role="img" aria-label="Software product box"></div>
        <div class="offer-body"><h4>Lorem ipsum dolor sit amet, consectetur elit...</h4><p>Lorem ipsum dolor sit amet, consectetur adipiscing elit, sed do eiusmod tempor incididunt ut labore et dolore.</p><a>Read more &raquo;</a><div class="ref">Shopping reference: Lorem ipsum dolor sit amet</div></div>
        <div class="price"><strong>£140.97</strong><span>Go to site</span></div>
      </article>
      <article class="offer">
        <div class="offer-image" role="img" aria-label="Software product box"></div>
        <div class="offer-body"><h4>Lorem ipsum dolor sit amet, consectetur elit...</h4><p>Lorem ipsum dolor sit amet, consectetur adipiscing elit, sed do eiusmod tempor incididunt ut labore et dolore.</p><a>Read more &raquo;</a><div class="ref">Shopping reference: Lorem ipsum dolor sit amet</div></div>
        <div class="price"><strong>£140.97</strong><span>Go to site</span></div>
      </article>
      <article class="offer">
        <div class="offer-image" role="img" aria-label="Software product box"></div>
        <div class="offer-body"><h4>Lorem ipsum dolor sit amet, consectetur elit...</h4><p>Lorem ipsum dolor sit amet, consectetur adipiscing elit, sed do eiusmod tempor incididunt ut labore et dolore.</p><a>Read more &raquo;</a><div class="ref">Shopping reference: Lorem ipsum dolor sit amet</div></div>
        <div class="price"><strong>£140.97</strong><span>Go to site</span></div>
      </article>
      <article class="offer">
        <div class="offer-image" role="img" aria-label="Software product box"></div>
        <div class="offer-body"><h4>Lorem ipsum dolor sit amet, consectetur elit...</h4><p>Lorem ipsum dolor sit amet, consectetur adipiscing elit, sed do eiusmod tempor incididunt ut labore et dolore.</p><a>Read more &raquo;</a><div class="ref">Shopping reference: Lorem ipsum dolor sit amet</div></div>
        <div class="price"><strong>£140.97</strong><span>Go to site</span></div>
      </article>
      <article class="offer">
        <div class="offer-image" role="img" aria-label="Software product box"></div>
        <div class="offer-body"><h4>Lorem ipsum dolor sit amet, consectetur elit...</h4><p>Lorem ipsum dolor sit amet, consectetur adipiscing elit, sed do eiusmod tempor incididunt ut labore et dolore.</p><a>Read more &raquo;</a><div class="ref">Shopping reference: Lorem ipsum dolor sit amet</div></div>
        <div class="price"><strong>£140.97</strong><span>Go to site</span></div>
      </article>

      <div class="pagination"><span>1</span><span>2</span><span>3</span><span>4</span><span>5</span><span>...</span><span class="next">NEXT</span></div>
    </section>
  </div>
</main>

<section class="safety">
  <div class="wrap">
    <div class="section-title">
      <h2>SAFETY SOFTWARE</h2>
      <div class="title-arrows">
        <span><svg width="6" height="8" viewBox="0 0 6 8"><path d="M5 0L1 4l4 4" stroke="#fff" stroke-width="1.5" fill="none"/></svg></span>
        <span><svg width="6" height="8" viewBox="0 0 6 8"><path d="M1 0l4 4-4 4" stroke="#fff" stroke-width="1.5" fill="none"/></svg></span>
      </div>
    </div>
    <div class="articles">
      <div class="article"><time>DECEMBER 12</time><h4>Lorem ipsum dolor sit amet, consectetur</h4><p>Lorem ipsum dolor sit amet, consectetur adipiscing elit sed do.</p><span class="btn-small">MORE</span></div>
      <div class="article"><time>DECEMBER 11</time><h4>Lorem ipsum dolor sit amet, consectetur</h4><p>Lorem ipsum dolor sit amet, consectetur adipiscing elit sed do.</p><span class="btn-small">MORE</span></div>
      <div class="article"><time>DECEMBER 10</time><h4>Lorem ipsum dolor sit amet, consectetur</h4><p>Lorem ipsum dolor sit amet, consectetur adipiscing elit sed do.</p><span class="btn-small">MORE</span></div>
      <div class="article"><time>DECEMBER 09</time><h4>Lorem ipsum dolor sit amet, consectetur</h4><p>Lorem ipsum dolor sit amet, consectetur adipiscing elit sed do.</p><span class="btn-small">MORE</span></div>
    </div>
  </div>
</section>

<section class="contact">
  <div class="wrap">
    <div class="contact-title"><h2>GET IN TOUCH</h2></div>
    <p class="contact-intro">If you'd like to get in touch with us about future projects, or have any questions at all, feel free to send us a message with the details below.</p>
    <div class="contact-form">
      <div class="contact-info">
        <div class="line"><svg width="10" height="10" viewBox="0 0 24 24"><circle cx="12" cy="8" r="5" fill="#fff"/><path d="M3 22c0-5 4-8 9-8s9 3 9 8z" fill="#fff"/></svg>Lorem ipsum dolor sit</div>
        <div class="field">Name</div>
        <div class="field">Email</div>
      </div>
      <div class="message">Message</div>
      <div class="contact-email">
        <div class="line"><svg width="12" height="9" viewBox="0 0 12 9"><rect width="12" height="9" fill="#fff"/><path d="M0 0l6 5 6-5" stroke="#1f4f8e" fill="none"/></svg>info@shieldwisehub.example</div>
        <div class="btn-send">SEND</div>
      </div>
    </div>
    <div class="social">
      <span><i></i>Chirpline</span><span><i></i>Friendbook</span><span><i></i>ClipTube</span><span><i></i>Circlely</span><span><i></i>Linkwork</span>
    </div>
  </div>
</section>

<footer class="site-footer">© 2013 Shieldwise Hub. All Rights Reserved. &nbsp;•&nbsp; Privacy Policy &nbsp;•&nbsp; Legal &nbsp;•&nbsp; Site Map</footer>

</body>
</html>
```